Financial Planner Marketing Post Card

I'm a Financial Planner and Managing Principal of our Washington DC office (we're a boutique firm based out of California).The name of my firm is The Harborstone Group, LLC. We specialize in investment strategies and Estate Planning. We offer everything from Estate Planning to Education Planning to Risk Management along with Insurance Planning. But I want my post card to really highlight is the main product I'm trying to sell with are the Fiduciary Standards of Being a RWA (Registered Wealth Advisor). I will attach a file with the Fiduciary Standards, along with a list of my service and products, company logo, along with a personal slogan. I would like for there to be room on my post card for my photo as well. I would like to use both sides of the post card with color; along with room for the BQRS postage.

```html
<!DOCTYPE html>
<html lang="en">
<head>
<meta charset="utf-8">
<title>Harborstone Group Postcard</title>
<link rel="stylesheet" href="https://fonts.googleapis.com/css2?family=Poppins:wght@700&family=Open+Sans:ital,wght@0,400;0,600;0,700;1,600&family=Open+Sans+Condensed:wght@700&family=Cinzel:wght@700&display=swap">
<style>
:root{
  --navy:#1f3f6e;
  --navy-deep:#163258;
  --yellow:#f4e21a;
  --aqua:#c6eaec;
  --aqua-light:#e4f5f6;
  --ink:#1d1d1f;
  --white:#ffffff;
  --photo-warm:#b7c6d3;
  --photo-cool:#7f9cb4;
  --backdrop:#e9dcc6;
}
*{box-sizing:border-box;margin:0;padding:0}
html,body{width:1200px;height:390px;overflow:hidden;background:var(--backdrop);font-family:"Open Sans",Arial,sans-serif;color:var(--ink)}
.card{position:absolute;top:28px;width:515px;height:330px;overflow:hidden;box-shadow:0 2px 6px rgba(0,0,0,.25)}
.card--front{left:60px;background:var(--aqua)}
.card--back{left:622px;background:linear-gradient(180deg,#fff 0%,#fff 55%,var(--aqua) 100%)}

/* front */
.front__header{position:absolute;inset:0 0 auto 0;height:62px;z-index:3;color:var(--white);font-family:"Poppins",Arial,sans-serif;font-weight:700;font-size:20px;line-height:25px;text-align:center;padding-top:7px;letter-spacing:.2px}
.front__header em{font-style:normal;color:var(--yellow)}
.front__band{position:absolute;inset:0 0 auto 0;height:62px;background:var(--navy);z-index:1}
.front__swoosh{position:absolute;left:0;top:58px;width:515px;height:28px;z-index:2}
.front__photo{position:absolute;left:0;top:60px;width:250px;height:270px;background:linear-gradient(160deg,var(--photo-warm) 0%,#dfe7ee 45%,var(--photo-cool) 100%)}
.height-box{position:absolute;left:86px;top:206px;width:162px;background:var(--navy);border:3px solid var(--yellow);color:var(--white);font-size:9.8px;line-height:14px;padding:5px 6px;white-space:nowrap;z-index:3}
.height-box b{color:var(--yellow);font-weight:700}
.advisor{position:absolute;left:260px;top:82px;width:150px}
.advisor__name{color:var(--navy);font-family:"Open Sans Condensed","Open Sans",sans-serif;font-weight:700;font-size:13px;line-height:16px}
.advisor__creds{margin-top:3px;font-size:8.2px;line-height:10.6px;font-weight:600;font-style:italic;color:var(--navy)}
.portrait-slot{position:absolute;left:410px;top:70px;width:90px;height:112px;background:#231f20;color:var(--white);font-family:"Poppins",Arial,sans-serif;font-weight:700;font-size:13px;line-height:16px;display:flex;align-items:center;justify-content:center;text-align:center;z-index:3}
.cta{position:absolute;left:260px;top:200px;width:245px;color:var(--navy)}
.cta__lead{font-size:8.5px;font-weight:700;text-transform:uppercase;line-height:12px}
.cta__lead span{font-size:10px}
.contact{list-style:none;margin-top:4px;font-size:9.8px;line-height:13px;color:var(--navy)}
.contact li{display:flex;align-items:center;gap:4px}
.contact svg{width:9px;height:9px;flex:none}
.address{position:absolute;left:268px;top:274px;font-size:8px;line-height:10.5px;color:var(--navy)}
.address svg{width:7px;height:9px;vertical-align:-1px}
.brand{position:absolute;display:flex;align-items:center;gap:5px;color:var(--navy);font-family:"Open Sans",sans-serif;font-weight:700;text-transform:uppercase}
.brand__dot{border-radius:50%;background:var(--navy);flex:none}
.card--front .brand{left:374px;top:284px;font-size:8.5px;line-height:11px;width:135px}
.card--front .brand__dot{width:22px;height:22px}

/* back */
.back__title{position:absolute;left:12px;top:18px;font-family:"Cinzel",Georgia,serif;font-weight:700;font-size:25px;line-height:26px;color:var(--navy)}
.card--back .brand{left:262px;top:26px;font-size:9px;line-height:11px;width:140px}
.card--back .brand__dot{width:24px;height:24px}
.back__address{position:absolute;left:272px;top:66px;font-size:8px;line-height:10px;color:var(--navy)}
.back__address svg{width:7px;height:9px;vertical-align:-1px}
.indicia{position:absolute;left:424px;top:12px;width:84px;height:66px;border:1.5px solid var(--ink);font-family:Arial,sans-serif;font-size:9.5px;line-height:12px;text-align:center;padding-top:2px;text-transform:uppercase}
.indicia b{font-weight:700}
.section-bar{position:absolute;left:0;width:255px;height:18px;background:linear-gradient(90deg,var(--navy) 55%,rgba(31,63,110,0) 100%);color:var(--white);font-family:"Open Sans Condensed","Open Sans",sans-serif;font-weight:700;font-size:12.5px;line-height:18px;padding-left:6px}
.section-bar--standards{top:76px}
.section-bar--services{top:205px}
.standards{position:absolute;left:8px;top:98px;width:240px;list-style:none;font-size:8px;line-height:10px}
.standards li{padding-left:8px;position:relative}
.standards li::before{content:"";position:absolute;left:0;top:3.5px;width:4px;height:4px;border-radius:50%;background:var(--ink)}
.services{position:absolute;left:14px;top:228px;list-style:none;font-family:"Open Sans Condensed","Open Sans",sans-serif;font-weight:700;font-size:10.5px;line-height:15.2px;color:var(--ink)}
.services li{display:flex;align-items:center;gap:5px}
.services svg{width:11px;height:11px;flex:none}
.back__photo{position:absolute;left:253px;top:132px;width:262px;height:62px;background:linear-gradient(100deg,#6f8a5a 0%,#c9c3b2 45%,#8aa26c 100%)}
.back__contact{position:absolute;left:253px;top:194px;width:262px;height:62px;background:var(--navy);color:var(--white);font-size:8.6px;line-height:11px;padding:6px 0 0 16px;white-space:nowrap}
.back__contact p:first-child{margin-bottom:2px}
.address-block{position:absolute;left:300px;top:276px;font-family:Arial,sans-serif;font-size:7.5px;line-height:10px}
.address-block .route{margin-left:30px;margin-bottom:12px}
.address-block b{display:block;font-weight:700}
</style>
</head>
<body>

<section class="card card--front" aria-label="Postcard front">
  <div class="front__band" aria-hidden="true"></div>
  <h1 class="front__header">Add someone with <em>HEIGHT</em> to your<br>personal team of professionals</h1>
  <div class="front__photo" role="img" aria-label="Photo of an advisor meeting with a smiling couple"></div>
  <svg class="front__swoosh" viewBox="0 0 515 28" preserveAspectRatio="none" aria-hidden="true">
    <path d="M0 2 C140 22 300 26 515 2 L515 0 L0 0 Z" fill="var(--navy)"/>
    <path d="M0 2 C140 22 300 26 515 2" fill="none" stroke="var(--aqua-light)" stroke-width="3"/>
  </svg>
  <div class="height-box">
    <div><b>H:</b> Honest</div>
    <div><b>E:</b> Experienced &amp; Educated</div>
    <div><b>I:</b> Integrity</div>
    <div><b>G:</b> a belief in “giving first”</div>
    <div><b>H:</b> Hardworking</div>
    <div><b>T:</b> Trustworthy</div>
  </div>

  <div class="advisor">
    <p class="advisor__name">Dale Whitmore III, RWA, CIMA, CTFA</p>
    <p class="advisor__creds">Registered Wealth Advisor, Certified Investment Management Analyst, Certified Trust and Financial Advisor-Managing Principal and Sr. Financial Advisor</p>
  </div>
  <div class="portrait-slot">YOUR<br>PICTURE<br>HERE</div>

  <div class="cta">
    <p class="cta__lead"><span>C</span>all or email to request<br>complementary planning session</p>
    <ul class="contact">
      <li><svg viewBox="0 0 10 10"><circle cx="5" cy="5" r="4.5" fill="none" stroke="var(--navy)"/><path d="M3.3 2.6l1 1-.5.7a3 3 0 0 0 1.9 1.9l.7-.5 1 1-.7.8C4.9 7.3 2.7 5.1 2.6 3.3z" fill="var(--navy)"/></svg>(555)214-0738</li>
      <li><svg viewBox="0 0 10 10"><rect x="1" y="2" width="8" height="6" fill="none" stroke="var(--navy)"/><path d="M1 2l4 3.5L9 2" fill="none" stroke="var(--navy)"/></svg>dwhitmore@harborstonellc.com</li>
      <li><svg viewBox="0 0 10 10"><circle cx="5" cy="5" r="4.5" fill="var(--navy)"/><path d="M.5 5h9M5 .5c-2 2.5-2 6.5 0 9M5 .5c2 2.5 2 6.5 0 9" fill="none" stroke="var(--white)" stroke-width=".6"/></svg>www.harborstonedc.com</li>
    </ul>
  </div>

  <p class="address"><svg viewBox="0 0 7 9"><path d="M3.5 0a3 3 0 0 1 3 3c0 2-3 6-3 6S.5 5 .5 3a3 3 0 0 1 3-3z" fill="var(--navy)"/><circle cx="3.5" cy="3" r="1" fill="var(--aqua)"/></svg> 4400 Linden Street NW<br>Suite 315<br>Washington, DC 20010</p>
  <div class="brand"><span class="brand__dot"></span><span>The Harborstone Group, LLC</span></div>
</section>

<section class="card card--back" aria-label="Postcard back">
  <h2 class="back__title">You Interests<br>Comes First</h2>
  <div class="brand"><span class="brand__dot"></span><span>The Harborstone Group, LLC</span></div>
  <p class="back__address"><svg viewBox="0 0 7 9"><path d="M3.5 0a3 3 0 0 1 3 3c0 2-3 6-3 6S.5 5 .5 3a3 3 0 0 1 3-3z" fill="var(--navy)"/><circle cx="3.5" cy="3" r="1" fill="#fff"/></svg> 4400 Linden Street NW<br>Suite 315<br>Washington, DC 20010</p>
  <div class="indicia">Prsrt Std<br>ECRWSS<br>U.S. Postage<br><b>Paid</b><br>BQRS Retail</div>

  <h3 class="section-bar section-bar--standards">Fiduciary Standards:</h3>
  <ul class="standards">
    <li>To place the interests of clients ahead of the interests of the adviser and its personnel;</li>
    <li>To act with the skill, loyalty, reasonable care, diligence, and good judgment of a professional;</li>
    <li>To provide full and fair disclosure of all important facts;</li>
    <li>To avoid conflicts of interest;</li>
    <li>To not mislead clients;</li>
    <li>To disclose all conflicts of interest to clients and fairly manage, in the client’s favor, any unavoidable conflicts.</li>
  </ul>

  <h3 class="section-bar section-bar--services">Company Services:</h3>
  <ul class="services">
    <li><svg viewBox="0 0 11 11"><circle cx="5.5" cy="5.5" r="4.8" fill="none" stroke="var(--ink)"/><path d="M3 5.6l1.8 1.8L8.2 3.8" fill="none" stroke="var(--ink)" stroke-width="1.2"/></svg>Retirement Savings &amp; Income Planning</li>
    <li><svg viewBox="0 0 11 11"><circle cx="5.5" cy="5.5" r="4.8" fill="none" stroke="var(--ink)"/><path d="M3 5.6l1.8 1.8L8.2 3.8" fill="none" stroke="var(--ink)" stroke-width="1.2"/></svg>Education Planning</li>
    <li><svg viewBox="0 0 11 11"><circle cx="5.5" cy="5.5" r="4.8" fill="none" stroke="var(--ink)"/><path d="M3 5.6l1.8 1.8L8.2 3.8" fill="none" stroke="var(--ink)" stroke-width="1.2"/></svg>Risk Management &amp; Insurance Planning</li>
    <li><svg viewBox="0 0 11 11"><circle cx="5.5" cy="5.5" r="4.8" fill="none" stroke="var(--ink)"/><path d="M3 5.6l1.8 1.8L8.2 3.8" fill="none" stroke="var(--ink)" stroke-width="1.2"/></svg>Investment Planning</li>
    <li><svg viewBox="0 0 11 11"><circle cx="5.5" cy="5.5" r="4.8" fill="none" stroke="var(--ink)"/><path d="M3 5.6l1.8 1.8L8.2 3.8" fill="none" stroke="var(--ink)" stroke-width="1.2"/></svg>Tax Planning</li>
    <li><svg viewBox="0 0 11 11"><circle cx="5.5" cy="5.5" r="4.8" fill="none" stroke="var(--ink)"/><path d="M3 5.6l1.8 1.8L8.2 3.8" fill="none" stroke="var(--ink)" stroke-width="1.2"/></svg>Estate Planning</li>
  </ul>

  <div class="back__photo" role="img" aria-label="Photo of a laughing senior couple outdoors"></div>
  <div class="back__contact">
    <p>Call or email to request complementary planning session</p>
    <p>(555)214-0738</p>
    <p>dwhitmore@harborstonellc.com</p>
    <p>www.harborstonedc.com</p>
  </div>

  <div class="address-block">
    <p class="route">*****************ECRWSS****</p>
    <b>Local</b>
    <b>Postal Customer</b>
  </div>
</section>

</body>
</html>
```